Trendy eye catching business card for lawn mowing business

Verge Kings, a local community lawn mowing service, requires an eye catching trendy business card to drop into letterboxes.

We could simply throw something together from a Microsoft Word template, but we are wanting something more than this. Some other business’ images are attached for some inspiration.

We are requiring the card to have Verge Kings with our slogan, Call The Pembrys. In addition, provide details with that we are a local, affordable lawn mowing service, and for other gardening matters to simply just ask!
Plus the relevant contact details, phone, email, social media.

Target Market(s)

Local community members who require assistance with their garden care

Industry/Entity Type

Gardening

Contact Information for Business Card

the name VERGE KINGS is our logo
telephone logo 0438 215 967
email logo vergekings@postbox-demo.com
Instagram logo vergekings
Facebook logo vergekings.sth
Lawn Mowing Service
Local Affordable
edge trim, blow and clipping removal included.
Other gardening matters, just ask!

Font styles to use
Serif
Sans Serif
Decorative
Script

Colors
9bcb3c
ffffff

Requirements
Must have
• All the details listed in Business Card Details.
Make these words prominent:
Verge Kings
Lawn Mowing Service
Local
Affordable
Nice to have
• Our slogan ‘Call The Pembrys’ incorporated.
Different colour background for front and reverse side
Greens, white and black colours
Subtle grass blades images incorporated
Should not have
• No images of lawnmowers.
No images of men/cartoons.
No using initials for Verge Kings

```html
<!DOCTYPE html>
<html lang="en">
<head>
<meta charset="utf-8">
<title>Verge Kings – Business Card</title>
<link rel="stylesheet" href="https://fonts.googleapis.com/css2?family=Archivo+Black&family=Quicksand:wght@400;500;600;700&display=swap">
<style>
  :root {
    --lawn-green: #9bcb3c;
    --charcoal: #4a4a4a;
    --chevron: #3d3d3d;
    --white: #ffffff;
    --stage: #1f1f1f;
  }
  * { box-sizing: border-box; margin: 0; padding: 0; }
  html, body { width: 1200px; height: 900px; overflow: hidden; }
  body {
    background: var(--stage);
    position: relative;
    font-family: "Quicksand", sans-serif;
  }
  .card {
    position: absolute;
    width: 720px;
    height: 412px;
    overflow: hidden;
  }

  /* Front side */
  .card-front {
    left: 340px;
    top: 40px;
    background: var(--lawn-green);
    color: var(--white);
    text-align: center;
  }
  .front-brand {
    margin-top: 58px;
    font-family: "Archivo Black", sans-serif;
    font-size: 46px;
    line-height: 1;
    letter-spacing: 1px;
  }
  .front-slogan {
    margin-top: 8px;
    font-size: 15px;
    font-weight: 600;
    letter-spacing: 2px;
    text-transform: uppercase;
  }
  .service-list {
    list-style: none;
    margin-top: 16px;
    font-family: "Archivo Black", sans-serif;
    font-size: 25px;
    line-height: 29px;
  }
  .chev { color: var(--chevron); font-size: 22px; padding: 0 6px; }
  .front-rule {
    width: 560px;
    height: 2px;
    background: var(--white);
    margin: 12px auto 14px;
    border: 0;
  }
  .front-note {
    font-size: 17px;
    font-weight: 500;
    line-height: 24px;
  }

  /* Back side */
  .card-back {
    left: 190px;
    top: 470px;
    background: var(--white);
  }
  .back-swoosh { position: absolute; inset: 0; }
  .back-brand {
    position: absolute;
    left: 50px;
    top: 48px;
  }
  .back-brand-name {
    font-family: "Archivo Black", sans-serif;
    color: var(--lawn-green);
    font-size: 54px;
    line-height: 0.95;
    letter-spacing: 1px;
  }
  .back-slogan {
    margin-top: 10px;
    color: var(--charcoal);
    font-size: 20px;
    font-weight: 600;
    letter-spacing: 2px;
    text-transform: uppercase;
  }
  .person {
    position: absolute;
    right: 40px;
    top: 214px;
    text-align: right;
    color: var(--white);
  }
  .person-name {
    color: var(--lawn-green);
    font-size: 29px;
    font-weight: 700;
    letter-spacing: 1px;
    line-height: 1;
  }
  .person-role { font-size: 18px; font-weight: 500; margin-top: 4px; }
  .contact-list {
    list-style: none;
    margin-top: 12px;
    font-size: 17px;
    font-weight: 500;
    line-height: 25px;
  }
  .contact-list li { display: flex; justify-content: flex-end; align-items: center; gap: 12px; }
  .contact-list li.gap-top { margin-top: 8px; }
  .contact-icon { width: 20px; height: 20px; flex: none; }
  .social-mark {
    width: 18px; height: 18px; flex: none;
    background: var(--lawn-green);
    border-radius: 3px;
    margin: 0 1px;
  }
</style>
</head>
<body>

<section class="card card-front" aria-label="Card front">
  <h1 class="front-brand">VERGE KINGS</h1>
  <p class="front-slogan">Call The Pembrys</p>
  <ul class="service-list">
    <li><span class="chev">›</span>VERGE KINGS<span class="chev">‹</span></li>
    <li><span class="chev">›</span>LAWN MOWING SERVICE<span class="chev">‹</span></li>
    <li><span class="chev">›</span>LOCAL<span class="chev">‹</span></li>
    <li><span class="chev">›</span>AFFORDABLE<span class="chev">‹</span></li>
  </ul>
  <hr class="front-rule">
  <p class="front-note">Edge trim, blow and clipping removal included.<br>Other gardening matters, JUST ASK!</p>
</section>

<section class="card card-back" aria-label="Card back">
  <svg class="back-swoosh" viewBox="0 0 720 412" width="720" height="412" aria-hidden="true">
    <path d="M0,105 Q20,330 340,298 Q560,272 720,86 L720,412 L0,412 Z" fill="var(--lawn-green)"/>
    <path d="M0,300 Q300,322 720,92 L720,412 L0,412 Z" fill="var(--charcoal)"/>
    <path d="M0,300 Q300,322 720,92" fill="none" stroke="var(--white)" stroke-width="4"/>
  </svg>

  <div class="back-brand">
    <p class="back-brand-name">VERGE<br>KINGS</p>
    <p class="back-slogan">Call The Pembrys</p>
  </div>

  <div class="person">
    <h2 class="person-name">DALE CORRIGAN</h2>
    <p class="person-role">Director/ Owner</p>
    <ul class="contact-list">
      <li>0438 215 967
        <svg class="contact-icon" viewBox="0 0 20 20" aria-hidden="true">
          <circle cx="10" cy="10" r="8.5" fill="none" stroke="var(--lawn-green)" stroke-width="1.6"/>
          <path d="M7 6.5 L8.5 6.5 L9.2 8.4 L8.3 9.3 Q9.2 11.2 10.9 11.9 L11.8 11 L13.6 11.7 L13.6 13.2 Q9 13.6 6.6 8.2 Z" fill="var(--lawn-green)"/>
        </svg>
      </li>
      <li>vergekings@postbox-demo.com
        <svg class="contact-icon" viewBox="0 0 20 20" aria-hidden="true">
          <rect x="2" y="4.5" width="16" height="11" fill="none" stroke="var(--lawn-green)" stroke-width="1.6"/>
          <path d="M2 4.5 L10 11 L18 4.5" fill="none" stroke="var(--lawn-green)" stroke-width="1.6"/>
        </svg>
      </li>
      <li class="gap-top">@vergekings <span class="social-mark"></span></li>
      <li>/vergekings.sth <span class="social-mark"></span></li>
    </ul>
  </div>
</section>

</body>
</html>
```